I need a flyer made , the flyer can be one page or two pages or three pages . I will be posting this on Instagram and social media platforms. I am a luxury home builder , I am looking to hire a construction project manager . Below are some examples and ideas what can be on the flyer

We’re looking for a construction project manager who’s passionate about building luxury homes at the highest standards
We’re hiring construction project manager
* Experience 5+ years in residential project management with a strong portfolio of completed homes.
* location : Bergen County NJ
* excellent leadership skills, leads teams with confidence and clarity
* communicates seamlessly with architects , engineers, designers and clients
*knows how to manage budgets and timelines without compromising quality
*solves problems with a positive solution first mindset
* pays attention to every detail because in luxury the small things are the big things

Apply now , link in bio or DM to connect.

My logo is attached, my web site www.ridgelanebuilders.com
My style is modern but still warm and inviting. I like a clean classy look .
Updates

Please don’t add any images of chairs or people to the flyer , I do not want people on my flyer. Do not add standard images of offices and houses , we are luxury builders , we build homes over 2 million dollars. Keep a classy , simple modern look . High end .

You can add a white hard hat with my logo on it for a image , this is a suggestion does not have to be on my flyer ,

```html
<!DOCTYPE html>
<html lang="en">
<head>
<meta charset="utf-8">
<title>Ridgelane Builders – Construction Project Manager</title>
<link rel="stylesheet" href="https://fonts.googleapis.com/css2?family=Montserrat:wght@400;500;600;700&display=swap">
<style>
  :root {
    --stage: #e0e0e0;
    --paper: #ffffff;
    --ink: #161616;
    --black: #000000;
    --taupe: #b3a291;
  }
  * { box-sizing: border-box; margin: 0; padding: 0; }
  html, body { width: 1200px; height: 841px; overflow: hidden; }
  body {
    background: var(--stage);
    font-family: "Montserrat", Arial, sans-serif;
    color: var(--ink);
    position: relative;
  }
  .flyer {
    position: absolute;
    top: 148px;
    width: 629px;
    height: 629px;
    background: var(--paper);
    transform: scale(0.8584);
    transform-origin: top left;
    box-shadow: 0 2px 8px rgba(0,0,0,0.18);
    overflow: hidden;
  }
  .flyer--photo { left: 43px; }
  .flyer--details { left: 616px; }
  .flyer > svg.shapes { position: absolute; inset: 0; width: 629px; height: 629px; }

  .brand {
    position: absolute;
    font-weight: 500;
    font-size: 26px;
    letter-spacing: 1px;
    text-transform: uppercase;
    white-space: nowrap;
    z-index: 2;
  }
  .flyer--photo .brand { left: 38px; top: 50px; color: var(--ink); }
  .flyer--details .brand { left: 44px; top: 56px; color: var(--paper); }

  .badge {
    position: absolute;
    border-radius: 50%;
    background: var(--taupe);
    border: 4px solid var(--paper);
    color: var(--paper);
    font-weight: 700;
    display: flex; align-items: center; justify-content: center;
    text-align: center;
    line-height: 1.05;
    z-index: 3;
  }
  .flyer--photo .badge { left: 20px; top: 276px; width: 164px; height: 164px; font-size: 29px; }
  .flyer--details .badge { left: 448px; top: 10px; width: 114px; height: 114px; font-size: 21px; }

  .job-title { position: absolute; line-height: 1; color: var(--ink); white-space: nowrap; z-index: 2; }
  .job-title__main { display: block; font-weight: 700; }
  .job-title__sub { display: block; font-weight: 400; }
  .flyer--photo .job-title { left: 27px; top: 448px; }
  .flyer--photo .job-title__main { font-size: 46px; letter-spacing: -0.5px; }
  .flyer--photo .job-title__sub { font-size: 37px; margin-top: 4px; letter-spacing: -0.5px; }
  .flyer--details .job-title { left: 23px; top: 180px; }
  .flyer--details .job-title__main { font-size: 38px; letter-spacing: -1px; }
  .flyer--details .job-title__sub { font-size: 31px; margin-top: 2px; letter-spacing: -0.6px; }

  .requirements {
    position: absolute; left: 24px; top: 266px; width: 352px;
    list-style: none; font-size: 10.6px; line-height: 14.2px; color: var(--ink);
    z-index: 2;
  }
  .requirements li { position: relative; padding-left: 10px; }
  .requirements li::before {
    content: ""; position: absolute; left: 1px; top: 4px;
    border-left: 5px solid var(--ink);
    border-top: 3.5px solid transparent; border-bottom: 3.5px solid transparent;
  }
  .requirements strong { font-weight: 700; }

  .team-photo {
    position: absolute; left: 378px; top: 134px; width: 249px; height: 306px;
    background: linear-gradient(180deg, #f2f2f2 0%, #c6c6c8 55%, #8e8f94 100%);
  }
  .gallery-band { position: absolute; left: 0; top: 440px; width: 629px; height: 148px; background: var(--black); }
  .gallery-thumb { position: absolute; top: 450px; width: 140px; height: 85px; border: 2px solid var(--paper); }
  .gallery-thumb--plan { left: 24px; background: linear-gradient(135deg, #f4f4f4, #cfd3d6); }
  .gallery-thumb--frame { left: 173px; background: linear-gradient(180deg, #b9cfe3, #b48a5e); }
  .gallery-thumb--render { left: 322px; background: linear-gradient(180deg, #dfe8ee, #8fc6d6); }
  .gallery-thumb--home { left: 470px; background: linear-gradient(180deg, #9fc4e8, #e8e8e8 55%, #6fa34a); }

  .cta-bar { position: absolute; left: 0; top: 542px; width: 629px; height: 46px; display: flex; }
  .cta-bar__apply {
    width: 204px; background: var(--black); color: var(--paper);
    font-size: 22px; display: flex; align-items: center; justify-content: center;
  }
  .cta-bar__contact {
    flex: 1; background: var(--taupe); color: var(--paper);
    font-size: 22px; display: flex; align-items: center; justify-content: center;
  }
  .website {
    position: absolute; right: 50px; top: 598px;
    font-size: 18px; font-weight: 700; letter-spacing: 0.2px; color: var(--ink);
  }
</style>
</head>
<body>

<section class="flyer flyer--photo">
  <svg class="shapes" viewBox="0 0 629 629">
    <defs>
      <linearGradient id="interiorTones" x1="0" y1="0" x2="0" y2="1">
        <stop offset="0" stop-color="#f4f3f2"/>
        <stop offset="0.55" stop-color="#e4e2df"/>
        <stop offset="1" stop-color="#d2b48e"/>
      </linearGradient>
    </defs>
    <polygon role="img" aria-label="Bright luxury living room interior with oak floors and marble fireplace wall"
      points="0,112 228,150 530,0 629,0 629,512 222,360 0,405" fill="url(#interiorTones)"/>
  </svg>
  <div class="brand">Ridgelane Builders</div>
  <div class="badge">WE ARE<br>HIRING!</div>
  <h1 class="job-title">
    <span class="job-title__main">CONSTRUCTION</span>
    <span class="job-title__sub">PROJECT MANAGER</span>
  </h1>
  <div class="cta-bar">
    <div class="cta-bar__apply">APPLY NOW</div>
    <div class="cta-bar__contact">Link in bio or DM to connect</div>
  </div>
  <div class="website">WWW.RIDGELANEBUILDERS.COM</div>
</section>

<section class="flyer flyer--details">
  <svg class="shapes" viewBox="0 0 629 629" aria-hidden="true">
    <polygon points="0,0 629,0 629,8 225,158 0,118" fill="#000000"/>
  </svg>
  <div class="team-photo" role="img" aria-label="Project management team in hard hats and suits"></div>
  <div class="brand">Ridgelane Builders</div>
  <div class="badge">WE ARE<br>HIRING!</div>
  <h1 class="job-title">
    <span class="job-title__main">CONSTRUCTION</span>
    <span class="job-title__sub">PROJECT MANAGER</span>
  </h1>
  <ul class="requirements">
    <li><strong>Experience 5+ years</strong> in residential project management with a strong portfolio of completed homes.</li>
    <li><strong>Location :</strong> Bergen County NJ</li>
    <li><strong>Excellent leadership</strong> skills, leads teams with confidence &amp; clarity</li>
    <li><strong>Communicates seamlessly</strong> with architects , engineers, designers and clients</li>
    <li>Knows how to <strong>manage budgets and timelines</strong> without compromising quality</li>
    <li><strong>Solves problems</strong> with a positive solution first mindset</li>
    <li>Pays <strong>attention to every detail</strong> because in luxury the small things are the big things</li>
  </ul>
  <div class="gallery-band"></div>
  <div class="gallery-thumb gallery-thumb--plan" role="img" aria-label="Architectural floor plans with hard hat"></div>
  <div class="gallery-thumb gallery-thumb--frame" role="img" aria-label="Timber-framed home under construction"></div>
  <div class="gallery-thumb gallery-thumb--render" role="img" aria-label="Modern home with pool being sketched"></div>
  <div class="gallery-thumb gallery-thumb--home" role="img" aria-label="Finished luxury home exterior"></div>
  <div class="cta-bar">
    <div class="cta-bar__apply">APPLY NOW</div>
    <div class="cta-bar__contact">Link in bio or DM to connect</div>
  </div>
  <div class="website">WWW.RIDGELANEBUILDERS.COM</div>
</section>

</body>
</html>
```